Torvend Ledger Hub (Account) WP Design

We need an Account (Profile) Wordpress design to add to tlh.co.uk.

The design should be based on https://tlh.co.uk/about/. The look and feel of the menu on the left.

The logic, after login the header menu will add another page:

Before Login:
Home / About / Trading / Support /

After Login
Home / About / Trading / Support / Account (Demo) - Logout

When you click on the / Account /

"Account Profile" page is loaded where you can change the settings etc.

"Account Profile" menu on the left should look the same as in / About / (https://tlh.co.uk/about/)

We need the following sub-pages under "Account Profile"

- Profile
- Transfers
- Reports
- Security
- API Key
- Affiliates

Now looking into each page:
-
- Profile (Should be split into individual or business) a user can choose whether how he want to run his account:

[Individual]

Personal Details
First Name:
Middle Name:
Family Name:
Citizenship:
Gender:
DOB:

[Attach File] (Government Issues ID, Passport, Driving License) - Verify

Contact Information
Phone: +44 207 318 4426 - Verify
E-Mail: sample@mailverno.com - Verify

Residential Address
Address line 1:
Address line 2:
Address line 3:
City:
Postcode:
Country:

[Attach File] (Utility Bill or Bank Statement) - Verify

[Business]

Company Name:
Registration Number:

Registered Address
Address line 1:
Address line 2:
Address line 3:
City:
Postcode:
Country:

[Attach File] (Certificate of Incorporation) - Verify
[Attach File] (Memorandum & Articles of Association)
[Attach File] (Shareholder Register)

Company Contact Information
Website:

-

- Transfers (Where a user can link a bank account to deposit or withdraw funds from the account)

Transfers

Add a bank account:

Please select the country where beneficiary’s bank is domicile: [Please select]
Please select the currency you wish to make transfers in: [Please select]

Full beneficiary name:
Full beneficiary address:
Beneficiary bank name:
Beneficiary bank address:
Beneficiary Bank Identification Code (BIC)/Routing Code:
Beneficiary IBAN number/account number:

[SAVE]

Deposti funds to TLH Bank Account
Amount of currency to be received e.g. 2345.67 [Please select: USD, EUR, GBP] :
Full beneficiary name: Torvend Ledger Hub Limited
Full beneficiary address: Brenmoor Court
7-9 Kelvane Road
London, United Kingdom
Beneficiary bank name:
Beneficiary bank address:
Beneficiary Bank Identification Code (BIC)/Routing Code: XXXXXXXXXX
Beneficiary IBAN number/account number: XXXXXXXXXXXXXXXXXXXXXXXXXX

Deposit coins to TLH Coin Account
Amount of coins to be received e.g. 2345.67 [Please select: BTC, LTC]:
TLH Coin Account: XXXXXXXXXXXXXXXXXXXXXXXXXXXXX

Applicable charges (?):
[Clear] [Continue]

Withdraw funds from TLH Bank Account
Amount of currency to be sent e.g. 2345.67 [Please select: USD, EUR, GBP] :

Withdraw coins from TLH Coin Account:
Amount of coins to be sent e.g. 2345.67 [Please select: BTC, LTC]:
Please specify you coin account: XXXXXXXXXXXXXXXXXXXXXXXXXXXXX

Applicable charges (?):
[Clear] [Continue]

-

- Reports

TBC
-

- Security

Change Password
Current Password:
New Password:
Confirm New Password:

Enable / Disable : Two-factor Authentication (SMS)

-

- API Key
TBC

-
- Affiliates

Unlimited earning potential!
You'll receive up to 10% commission on all trades made through your affiliate link.

Partner Affiliate Network
Simply apply to our program from your publisher account or click the "Join Now" button below.

Quorvelle.com - Join Now

```html
<!DOCTYPE html>
<html lang="en">
<head>
<meta charset="utf-8">
<title>Torvend Ledger Hub – Account Profile</title>
<link rel="stylesheet" href="https://fonts.googleapis.com/css2?family=Arimo:wght@400;700&family=Archivo+Black&family=Roboto:wght@300&display=swap">
<style>
:root{
  --brand:#0a9bd6;
  --ink:#333333;
  --muted:#666666;
  --soft:#999999;
  --line:#cccccc;
  --field:#d4d4d4;
  --band:#e6e6e6;
  --frame:#3a3a3a;
  --dark-btn:#4a4a4a;
  --alert:#e08a94;
  --white:#ffffff;
}
*{box-sizing:border-box;margin:0;padding:0}
html,body{width:863px;height:1200px;overflow:hidden;background:var(--frame)}
body{font-family:"Arimo",Arial,sans-serif;color:var(--ink)}
.stage{position:relative;width:790px;height:1099px;transform:scale(1.0924);transform-origin:0 0}
.abs{position:absolute}
.page{left:16px;top:0;width:758px;height:864px;background:var(--white)}

/* header */
.wordmark{left:86px;top:22px;font-size:11px;font-weight:400;color:var(--ink);white-space:nowrap}
.wordmark-dot{left:198px;top:24px;width:10px;height:10px;border-radius:50%;background:var(--brand)}
.main-nav{left:198px;top:42px;font-size:8px;color:var(--ink);white-space:nowrap}
.main-nav .current{color:var(--brand)}
.login-field{top:24px;height:18px;border:2px solid var(--alert);border-radius:2px;font-size:7.5px;color:var(--soft);padding:3px 4px}
.login-field .help{position:absolute;right:8px;top:2px;width:10px;height:10px;border:1px solid var(--field);border-radius:50%;font-size:6px;text-align:center;line-height:8px}
.btn{display:block;text-align:center;color:var(--white);font-size:7.5px;border-radius:3px}
.btn-login{left:631px;top:26px;width:34px;height:14px;line-height:14px;background:var(--dark-btn)}
.btn-signup{left:669px;top:26px;width:34px;height:14px;line-height:14px;background:var(--brand)}

/* ticker */
.ticker{left:16px;top:64px;width:758px;height:30px;background:var(--brand)}
.coin{left:167px;top:68px;width:20px;height:20px;border-radius:50%;background:var(--white)}
.stat{top:68px;color:var(--white);padding-left:8px;border-left:1px solid rgba(255,255,255,.4);height:22px;white-space:nowrap}
.stat .k{font-size:6.5px;display:block}
.stat .v{font-size:9.5px;display:block;margin-top:2px}

/* title band */
.title-band{left:16px;top:94px;width:758px;height:49px;background:var(--band);border-bottom:1px solid var(--line)}
.page-title{left:94px;top:108px;font-family:"Archivo Black","Arial Black",sans-serif;font-size:18px;color:#000}

/* side menu */
.side-menu{left:94px;top:168px;width:139px;list-style:none}
.side-menu li{height:24px;border-bottom:1px solid var(--line);font-size:10.5px;line-height:20px;position:relative}
.side-menu .expand{position:absolute;right:4px;top:4px;width:10px;height:10px;background:var(--soft)}

/* form */
.form-title{left:268px;top:166px;font-family:"Roboto",Arial,sans-serif;font-weight:300;font-size:22px;color:#555}
.section-head{left:269px;font-size:10.5px;color:var(--brand)}
.section-rule{left:268px;width:402px;border-top:1px dashed var(--brand)}
.label{right:435px;font-size:8px;color:var(--ink);text-align:right;white-space:nowrap}
.label.plain{right:auto;left:283px}
.input{left:369px;width:156px;height:20px;border:1px solid var(--field);font-size:7.5px;color:var(--soft);padding:5px 4px;white-space:nowrap;overflow:hidden}
.verify{left:532px;width:48px;height:18px;line-height:18px;background:var(--brand)}
.note{left:372px;font-size:7px;color:var(--soft);width:150px;line-height:9px}
.note::before{content:"•";margin-right:4px}
.checks{left:371px;font-size:7.5px;color:var(--soft);white-space:nowrap}
.box{display:inline-block;width:8px;height:8px;border:1px solid var(--soft);vertical-align:-1px;margin-right:5px}
.btn-submit{left:370px;top:811px;width:60px;height:17px;line-height:17px;background:var(--dark-btn);border-radius:0}

/* footer */
.footer{left:16px;top:864px;width:758px;height:208px;background:var(--brand)}
.foot-wordmark{left:86px;top:896px;font-size:10px;font-weight:400;color:var(--white);white-space:nowrap}
.foot-dot{left:186px;top:898px;width:9px;height:9px;border-radius:50%;background:var(--white)}
.copy{left:86px;top:942px;font-size:6.5px;line-height:9px;color:var(--white)}
.foot-head{top:888px;font-size:14px;font-weight:700;color:var(--white);white-space:nowrap}
.foot-links{top:912px;list-style:none;font-size:7.5px;line-height:9.6px;color:var(--white)}
.social{top:913px;width:18px;height:18px;border-radius:50%;background:var(--white)}
.tagline{left:330px;top:996px;width:370px;height:46px;background:linear-gradient(90deg,rgba(255,255,255,.08),rgba(255,255,255,.22),rgba(255,255,255,.08));border-radius:4px}
</style>
</head>
<body>
<div class="stage">
  <div class="abs page"></div>

  <header>
    <div class="abs wordmark">Torvend Ledger Hub</div>
    <div class="abs wordmark-dot"></div>
    <nav class="abs main-nav">Home - About - Trading - Support - <span class="current">Account (Demo)</span> - Logout</nav>
    <div class="abs login-field" style="left:453px;width:86px">Email<span class="help">?</span></div>
    <div class="abs login-field" style="left:541px;width:86px">Password<span class="help">?</span></div>
    <a class="abs btn btn-login">Log In</a>
    <a class="abs btn btn-signup">Sign Up</a>
  </header>

  <section>
    <div class="abs ticker"></div>
    <div class="abs coin"></div>
    <div class="abs stat" style="left:186px;border-left:0"><span class="k">Current Price</span><span class="v">$444.13</span></div>
    <div class="abs stat" style="left:258px"><span class="k">Daily Change</span><span class="v">-9.54 <small style="font-size:7px">-2.10%</small></span></div>
    <div class="abs stat" style="left:337px"><span class="k">Day's Range</span><span class="v">$440.00 - $457.30</span></div>
    <div class="abs stat" style="left:443px"><span class="k">Today's Open</span><span class="v">$453.57</span></div>
    <div class="abs stat" style="left:517px"><span class="k">24h Volume</span><span class="v">7194 BTC</span></div>
  </section>

  <div class="abs title-band"></div>
  <h1 class="abs page-title">Account Profile</h1>

  <ul class="abs side-menu">
    <li>Profile<span class="expand"></span></li>
    <li>Transfers</li>
    <li>Reports</li>
    <li>Security</li>
    <li>API Key</li>
    <li>Affiliates</li>
  </ul>

  <main>
    <h2 class="abs form-title">Individual Profile</h2>

    <div class="abs section-head" style="top:203px">Personal Details</div>
    <div class="abs section-rule" style="top:219px"></div>

    <span class="abs label" style="top:238px">First Name:</span><div class="abs input" style="top:232px"></div>
    <span class="abs label" style="top:266px">Middle Name:</span><div class="abs input" style="top:260px"></div>
    <span class="abs label" style="top:293px">Family Name:</span><div class="abs input" style="top:287px"></div>
    <span class="abs label" style="top:321px">Citizenship:</span><div class="abs input" style="top:315px"></div>
    <span class="abs label" style="top:349px">Gender:</span>
    <div class="abs checks" style="top:348px"><span class="box"></span>Male &nbsp;&nbsp;<span class="box"></span>Female</div>
    <span class="abs label" style="top:376px">DOB:</span><div class="abs input" style="top:370px">dd/mm/yyyy</div>
    <span class="abs label" style="top:404px">Attache File:</span><div class="abs input" style="top:398px">Driving License</div>
    <a class="abs btn verify" style="top:400px">Verify</a>
    <div class="abs note" style="top:426px">Government Issues ID, Passport, Driving License</div>

    <div class="abs section-head" style="top:476px">Contact Information</div>
    <div class="abs section-rule" style="top:492px"></div>

    <span class="abs label" style="top:511px">Phone:</span><div class="abs input" style="top:505px">+44 207 318 4426</div>
    <a class="abs btn verify" style="top:507px">Verify</a>
    <span class="abs label" style="top:538px">E-Mail:</span><div class="abs input" style="top:532px">sample@mailverno.com</div>
    <a class="abs btn verify" style="top:534px">Verify</a>
    <span class="abs label plain" style="top:566px">Residential Address</span>
    <span class="abs label" style="top:594px">Address line 1:</span><div class="abs input" style="top:588px"></div>
    <span class="abs label" style="top:622px">Address line 2:</span><div class="abs input" style="top:616px"></div>
    <span class="abs label" style="top:649px">Address line 3:</span><div class="abs input" style="top:643px"></div>
    <span class="abs label" style="top:677px">City:</span><div class="abs input" style="top:671px"></div>
    <span class="abs label" style="top:705px">Postcode:</span><div class="abs input" style="top:699px"></div>
    <span class="abs label" style="top:733px">Country:</span><div class="abs input" style="top:727px"></div>
    <span class="abs label" style="top:759px">Attach File:</span><div class="abs input" style="top:753px"></div>
    <a class="abs btn verify" style="top:755px">Verifiy</a>
    <div class="abs note" style="top:782px">Utility Bill or Bank Statement</div>

    <a class="abs btn btn-submit">Submit</a>
  </main>

  <footer>
    <div class="abs footer"></div>
    <div class="abs foot-wordmark">Torvend Ledger Hub</div>
    <div class="abs foot-dot"></div>
    <div class="abs copy">© 2014 Torvend Ledger Hub.<br>All rights reserved.</div>

    <div class="abs foot-head" style="left:300px">ABOUT US</div>
    <ul class="abs foot-links" style="left:300px">
      <li>Rulebook</li><li>Trading Fees</li><li>Partners</li><li>Security</li>
      <li>Terms of Service</li><li>Privacy Policy</li><li>Latest News</li>
    </ul>

    <div class="abs foot-head" style="left:462px">SUPPORT</div>
    <ul class="abs foot-links" style="left:462px">
      <li>What is Bitcoin?</li><li>How to buy a bitcoin?</li><li>How to sell a bitcoin?</li>
    </ul>

    <div class="abs foot-head" style="left:607px">FOLLOW TLH</div>
    <span class="abs social" style="left:607px"></span>
    <span class="abs social" style="left:632px"></span>
    <span class="abs social" style="left:658px"></span>
    <span class="abs social" style="left:683px"></span>

    <div class="abs tagline" role="img" aria-label="Hand-lettered white script slogan: Change the world one bitcoin at a time"></div>
  </footer>
</div>
</body>
</html>
```